Business Card design for construction company

I would like a business card design for a construction company - Harlow Constructions. I have attached the ai logo file for use. I would like the card to be very smart and clean and incorporate only white and the two colours in the logo. I would like the card to have two sides. One side can just have the logo, the other with the relevant information.

Target Market(s)

Building and Construction Clients

Industry/Entity Type

Business

Contact Information for Business Card

Name: Tom Pardoe
Company: Harlow Constructions Pty Limited
Address: 14 Mallee Crescent Carrow Vale 2093
Phone: 0427 531 068
Email: tomp@harlowbuild-example.com.au

Font styles to use
Serif
Sans Serif

Requirements
Must have
• Details noted above
• Logo as provided
• Colours as in logo
• Square edges
• A font that compliments the logo
Should not have
• Any colour other than white and those in logo
• Rounded edges

```html
<!DOCTYPE html>
<html lang="en">
<head>
<meta charset="utf-8">
<title>Tom Pardoe – Harlow Constructions Business Card</title>
<link rel="stylesheet" href="https://fonts.googleapis.com/css2?family=Michroma&family=Syncopate:wght@700&display=swap">
<style>
  :root {
    --brand-blue: #0aa9e8;
    --ink-grey: #5a5a5c;
    --paper: #ffffff;
  }
  html, body {
    margin: 0;
    padding: 0;
    width: 1200px;
    height: 686px;
    overflow: hidden;
    background: var(--paper);
  }
  .card {
    position: relative;
    width: 1200px;
    height: 686px;
    background: var(--paper);
  }
  .card__name {
    position: absolute;
    left: 113px;
    top: 134px;
    margin: 0;
    font-family: "Syncopate", "Arial Black", sans-serif;
    font-weight: 700;
    font-size: 47px;
    line-height: 1;
    letter-spacing: 1px;
    color: var(--brand-blue);
    text-transform: uppercase;
  }
  .contact {
    position: absolute;
    left: 106px;
    display: flex;
    align-items: center;
    height: 76px;
  }
  .contact__icon {
    width: 54px;
    height: 54px;
    fill: var(--ink-grey);
    flex: none;
  }
  .contact__divider {
    width: 3px;
    height: 76px;
    margin-left: 34px;
    background: var(--brand-blue);
    flex: none;
  }
  .contact__text {
    margin: 0 0 0 35px;
    font-family: "Michroma", "Eurostile", sans-serif;
    font-size: 30px;
    line-height: 1.1;
    letter-spacing: 2px;
    color: var(--ink-grey);
    text-transform: uppercase;
    font-style: normal;
  }
  .contact--address { top: 226px; }
  .contact--phone   { top: 349px; }
  .contact--email   { top: 473px; }
  .contact--email .contact__text { font-size: 26px; letter-spacing: 1.5px; }
</style>
</head>
<body>
<main class="card">
  <h1 class="card__name">Tom Pardoe</h1>

  <div class="contact contact--address">
    <svg class="contact__icon" viewBox="0 0 24 24" aria-hidden="true">
      <path d="M12 2a7 7 0 0 0-7 7c0 5.2 7 13 7 13s7-7.8 7-13a7 7 0 0 0-7-7zm0 9.6A2.6 2.6 0 1 1 12 6.4a2.6 2.6 0 0 1 0 5.2z"/>
    </svg>
    <span class="contact__divider"></span>
    <address class="contact__text">14 Mallee Crescent<br>Carrow Vale 2093</address>
  </div>

  <div class="contact contact--phone">
    <svg class="contact__icon" viewBox="0 0 24 24" aria-hidden="true">
      <path d="M6.6 10.8a15.1 15.1 0 0 0 6.6 6.6l2.2-2.2a1 1 0 0 1 1-.25 11.4 11.4 0 0 0 3.6.57 1 1 0 0 1 1 1V20a1 1 0 0 1-1 1A17 17 0 0 1 3 4a1 1 0 0 1 1-1h3.5a1 1 0 0 1 1 1c0 1.25.2 2.45.57 3.57a1 1 0 0 1-.25 1z"/>
    </svg>
    <span class="contact__divider"></span>
    <p class="contact__text">0427 531 068</p>
  </div>

  <div class="contact contact--email">
    <svg class="contact__icon" viewBox="0 0 24 24" aria-hidden="true">
      <path d="M3 5h18a1 1 0 0 1 1 1v.6l-10 6-10-6V6a1 1 0 0 1 1-1zm-1 3.9 10 6 10-6V18a1 1 0 0 1-1 1H3a1 1 0 0 1-1-1z"/>
    </svg>
    <span class="contact__divider"></span>
    <p class="contact__text">tomp@harlowbuild-example.com.au</p>
  </div>
</main>
</body>
</html>
```